Small Business Consulting Firm Needs Business Card Design

Need a sleek modern business card with 2 sides matching the colors of our logo. We will be placing these with a mailer we are sending out. These business cards will only ever be given to business owners. We operate helping businesses who are struggling with cash flow or finances. If the green and blue design needs to be moved to the right of "Harborline Crest Consulting" for aesthetic purposes that is ok. We will need an editable file if possible. We would like to include the reps name, email, website, and phone number. For now just use Peter Vance, pvance@harborlinecrest.com, www.harborlinecrest.com, and 833-555-0172.

```html
<!DOCTYPE html>
<html lang="en">
<head>
<meta charset="utf-8">
<title>Harborline Crest Consulting – Business Card</title>
<link href="https://fonts.googleapis.com/css2?family=Montserrat:wght@400;500;600&display=swap" rel="stylesheet">
<style>
  :root {
    --backdrop: #d9d9d7;
    --card: #262626;
    --card-edge: #6fbf3a;
    --green: #6ab23a;
    --blue: #1a7fc4;
    --text-light: #d6d6d6;
    --text-muted: #a8a8a8;
  }
  * { box-sizing: border-box; margin: 0; padding: 0; }
  html, body {
    width: 1200px; height: 801px; overflow: hidden;
    background: var(--backdrop);
    font-family: "Montserrat", sans-serif;
  }
  .sheet {
    width: 1200px; height: 801px;
    display: flex; align-items: center; justify-content: center; gap: 44px;
  }
  .card {
    position: relative;
    width: 540px; height: 309px;
    background: var(--card);
    box-shadow: 0 0 0 2px var(--card-edge), 0 14px 30px rgba(0,0,0,.25);
    border-radius: 2px;
    color: var(--text-light);
  }

  /* Front */
  .brand {
    position: absolute; left: 44px; top: 70px;
    display: flex; align-items: center; gap: 12px;
  }
  .brand-square { width: 22px; height: 22px; background: var(--green); }
  .brand-name {
    font-size: 17px; font-weight: 400; letter-spacing: 1.5px;
    text-transform: uppercase; color: var(--text-light); line-height: 1.25;
  }
  .rep {
    position: absolute; right: 58px; top: 108px; text-align: right;
  }
  .rep-name {
    font-size: 21px; font-weight: 500; letter-spacing: 1px;
    text-transform: uppercase; color: var(--green);
  }
  .rep-title { font-size: 15px; color: var(--text-light); margin-top: 2px; }
  .divider {
    position: absolute; left: 72px; right: 58px; top: 176px;
    height: 1.5px; background: var(--green);
  }
  .contacts {
    position: absolute; left: 72px; top: 196px;
    list-style: none; font-size: 12.5px; line-height: 21px; color: var(--text-light);
  }
  .contacts li { display: flex; align-items: center; gap: 9px; }
  .contacts svg { width: 12px; height: 12px; fill: var(--blue); flex: none; }

  /* Back */
  .back-brand {
    position: absolute; left: 0; right: 0; top: 118px;
    display: flex; align-items: center; justify-content: center; gap: 14px;
  }
  .back-brand .brand-square { width: 28px; height: 28px; }
  .back-brand .brand-name { font-size: 22px; }
  .back-web {
    position: absolute; left: 0; right: 0; bottom: 54px;
    text-align: center; font-size: 13px; letter-spacing: 2px; color: var(--text-light);
  }
</style>
</head>
<body>
<main class="sheet">
  <section class="card card-front" aria-label="Card front">
    <div class="brand">
      <span class="brand-square"></span>
      <span class="brand-name">Harborline Crest<br>Consulting</span>
    </div>
    <div class="rep">
      <div class="rep-name">Peter Vance</div>
      <div class="rep-title">Director</div>
    </div>
    <div class="divider"></div>
    <ul class="contacts">
      <li><svg viewBox="0 0 24 24"><path d="M6.6 10.8a15 15 0 0 0 6.6 6.6l2.2-2.2a1 1 0 0 1 1-.25 11.4 11.4 0 0 0 3.6.57 1 1 0 0 1 1 1V20a1 1 0 0 1-1 1A17 17 0 0 1 3 4a1 1 0 0 1 1-1h3.5a1 1 0 0 1 1 1c0 1.25.2 2.45.57 3.57a1 1 0 0 1-.25 1z"/></svg>833-555-0172</li>
      <li><svg viewBox="0 0 24 24"><path d="M2 5h20v14H2zm2 2v.5l8 5 8-5V7l-8 5z"/></svg>pvance@harborlinecrest.com</li>
      <li><svg viewBox="0 0 24 24"><circle cx="12" cy="12" r="10"/></svg>www.harborlinecrest.com</li>
    </ul>
  </section>

  <section class="card card-back" aria-label="Card back">
    <div class="back-brand">
      <span class="brand-square"></span>
      <span class="brand-name">Harborline Crest</span>
    </div>
    <div class="back-web">www.harborlinecrest.com</div>
  </section>
</main>
</body>
</html>
```